Velvetorchid Hair & Beauty Business Card

Velvetorchid Hair & Beauty is a boutique salon located in the picturesque Lake Taupo NZ. The salon is very luxurious, opulent gold gilded mirrors, chandelier lit, contemporary french decor, sets the mood to create beautiful hair, makeup and all beauty services. Just had a new logo design and now after a new business card.
Logo
14 Korowhai Street
Taupo
Phone (07) 548 6193
www.velvetorchid.co.nz
email hair@velvetorchid.co.nz
Marlena Swithin
Also need a space to put in Stylist name, date, appointment time. thanks;)
Another idea is we could incorporate the wallpaper in the back ground either on the back or front or use an ornate glided frame (around the edge of the card) like on my website where my brides photos flash.
Decided against the wall paper but at least you can see our colour theme for the salon.
Updates

Please check out my updated brief . Thanks :)

Target Market(s)

25-60 years plus, mainly mid age females , wanting the best possible service , high standard of workmanship and money not a problem.

Industry/Entity Type

Boutique

Requirements
Must have
• Gold and silver

```html
<!DOCTYPE html>
<html lang="en">
<head>
<meta charset="utf-8">
<title>Velvetorchid Hair &amp; Beauty – Business Card</title>
<link rel="stylesheet" href="https://fonts.googleapis.com/css2?family=Quicksand:wght@400;500&family=Lora:ital,wght@1,700&display=swap">
<style>
  :root {
    --page-bg: #e9e6e1;
    --gilt-dark: #6b4a12;
    --gilt-mid: #b8861f;
    --gilt-light: #f1cf6a;
    --card-white: #ffffff;
    --ink-grey: #5a5653;
    --ink-gold: #8f7a2e;
    --back-gold-light: #eadba0;
    --back-gold-dark: #c9b46a;
    --field-ink: #7d6a22;
    --clock-ink: rgba(255, 250, 225, 0.55);
  }
  * { box-sizing: border-box; margin: 0; padding: 0; }
  html, body {
    width: 1200px;
    height: 1000px;
    overflow: hidden;
    background: var(--page-bg);
  }
  .canvas {
    position: relative;
    width: 1200px;
    height: 1000px;
  }
  .card {
    position: absolute;
    left: 240px;
    width: 720px;
    height: 440px;
    box-shadow: 0 8px 24px rgba(0,0,0,0.18);
  }
  /* Front */
  .card-front { top: 40px; }
  .gilded-frame {
    position: absolute;
    inset: 0;
    background: radial-gradient(ellipse at 50% 50%, var(--gilt-light) 0%, var(--gilt-mid) 55%, var(--gilt-dark) 100%);
  }
  .front-panel {
    position: absolute;
    left: 100px;
    top: 92px;
    width: 520px;
    height: 256px;
    background: var(--card-white);
    box-shadow: inset 0 0 6px rgba(0,0,0,0.35);
    display: flex;
    align-items: center;
    justify-content: center;
    gap: 14px;
  }
  .brand-mark {
    width: 16px;
    height: 16px;
    border-radius: 50%;
    background: var(--ink-gold);
  }
  .brand-name {
    font-family: "Quicksand", sans-serif;
    font-weight: 400;
    font-size: 34px;
    color: var(--ink-grey);
    letter-spacing: 0.5px;
  }
  /* Back */
  .card-back {
    top: 520px;
    background: radial-gradient(ellipse at 60% 35%, var(--back-gold-light) 0%, var(--back-gold-dark) 100%);
    overflow: hidden;
  }
  .card-slit {
    position: absolute;
    left: 38px;
    top: 160px;
    width: 14px;
    height: 180px;
    background: #f4f1ea;
    box-shadow: inset 1px 0 3px rgba(0,0,0,0.25);
  }
  .contact-block {
    position: absolute;
    left: 0;
    right: 0;
    top: 18px;
    text-align: center;
    font-family: "Lora", serif;
    font-style: italic;
    font-weight: 700;
    color: var(--field-ink);
    opacity: 0.8;
  }
  .contact-line { font-size: 15px; line-height: 20px; }
  .contact-person { font-size: 24px; line-height: 30px; margin-top: 2px; }
  .flourish-area {
    width: 170px;
    height: 20px;
    margin: 4px auto 0;
    background: linear-gradient(90deg, transparent, rgba(125,106,34,0.45), transparent);
    border-radius: 10px;
  }
  .clock-icon {
    position: absolute;
    right: 60px;
    top: 168px;
    width: 160px;
    height: 190px;
  }
  .appointment-fields {
    position: absolute;
    left: 90px;
    right: 90px;
    top: 180px;
    font-family: "Lora", serif;
    font-style: italic;
    font-weight: 700;
    font-size: 30px;
    color: var(--field-ink);
  }
  .field-row {
    position: relative;
    height: 62px;
    border-bottom: 5px solid var(--field-ink);
    display: flex;
    align-items: flex-end;
    padding-bottom: 2px;
  }
  .field-row + .field-row { margin-top: 14px; }
  .field-time {
    position: absolute;
    left: 330px;
    bottom: 2px;
  }
</style>
</head>
<body>
<main class="canvas">

  <section class="card card-front">
    <div class="gilded-frame" role="img" aria-label="Ornate gold gilded picture frame around the card edge"></div>
    <div class="front-panel">
      <span class="brand-mark"></span>
      <span class="brand-name">Velvetorchid Hair &amp; Beauty</span>
    </div>
  </section>

  <section class="card card-back">
    <div class="card-slit"></div>

    <svg class="clock-icon" viewBox="0 0 160 190" aria-hidden="true" fill="none" stroke="var(--clock-ink)" stroke-width="8" stroke-linecap="round">
      <path d="M22 52 A26 26 0 0 1 58 22 Z" fill="var(--clock-ink)" stroke="none"/>
      <path d="M138 52 A26 26 0 0 0 102 22 Z" fill="var(--clock-ink)" stroke="none"/>
      <circle cx="80" cy="98" r="62"/>
      <line x1="80" y1="98" x2="80" y2="60"/>
      <line x1="80" y1="98" x2="106" y2="112"/>
      <line x1="40" y1="150" x2="28" y2="178"/>
      <line x1="120" y1="150" x2="132" y2="178"/>
    </svg>

    <div class="contact-block">
      <p class="contact-line">14 Korowhai Street, Taupo</p>
      <p class="contact-line">Phone (07) 548 6193 &middot; hair@velvetorchid.co.nz</p>
      <p class="contact-line">www.velvetorchid.co.nz</p>
      <p class="contact-person">Marlena Swithin</p>
      <div class="flourish-area" role="img" aria-label="Small gold scroll ornament"></div>
    </div>

    <div class="appointment-fields">
      <div class="field-row">stylist:</div>
      <div class="field-row">date:<span class="field-time">time:</span></div>
    </div>
  </section>

</main>
</body>
</html>
```